Promotional Ad/Flyer - KVP Leasing

A division of our company, KVP Leasing (kvp-leasing.example) is celebrating its 1-year anniversary in September and we would like to run a promotion. I am looking to have a promotional ad/flyer made-up for email mailings and LinkedIn posts and possibly have on our site. Have plenty of product photos to share if needed, not a prerequisite to use our product in the ad but open to it. Can also be cool graphics as well. We want to capture the viewers attention with the 30 DAYS FREE! The message is simple:
We are celebrating our 1-Year Anniversary by offering a Special Peak-Season Promotion!

FREE RENTALS for 30 days with a minimum 30-Day rental!

Valid from Sep. 1 - Dec. 31 & while supplies last.

Please contact our sales department for more details.

Email: rfq@kvp-leasing.example
Phone: +1-555-284-3917

```html
<!DOCTYPE html>
<html lang="en">
<head>
<meta charset="utf-8">
<title>KVP Leasing – 1-Year Anniversary Promotion</title>
<link rel="stylesheet" href="https://fonts.googleapis.com/css2?family=Josefin+Sans:wght@300;400;600;700&family=League+Spartan:wght@600;700;800&family=Arimo:wght@400;700&display=swap">
<style>
  :root {
    --brand-blue: #2f5aa8;
    --brand-blue-light: #4a76c4;
    --ink: #2b2f38;
    --ink-soft: #3d4250;
    --footer: #3e4453;
    --photo-light: #e6e8eb;
    --photo-mid: #cfd3d8;
    --white: #ffffff;
  }
  * { margin: 0; padding: 0; box-sizing: border-box; }
  html, body { width: 800px; height: 1200px; overflow: hidden; background: var(--white); }
  .flyer {
    position: relative; width: 800px; height: 1200px; overflow: hidden;
    background: var(--white);
    font-family: "Josefin Sans", sans-serif; color: var(--ink);
  }
  .hero-backdrop {
    position: absolute; inset: 0 0 300px 0;
    background: linear-gradient(100deg, #e9eaec 0%, #e3e5e8 45%, #d6d9dd 75%, #cbcfd4 100%);
  }
  .hero-photo {
    position: absolute; left: 380px; top: 170px; width: 420px; height: 720px;
    background: radial-gradient(ellipse at 55% 45%, #f4f5f6 0%, #dfe2e6 40%, #c9ccd1 70%, rgba(201,204,209,0) 100%);
  }
  .swoosh { position: absolute; left: 0; top: 740px; width: 800px; height: 180px; }

  .brand { position: absolute; left: 40px; top: 38px; }
  .brand-name {
    display: flex; align-items: center; gap: 14px;
    font-family: "Josefin Sans", sans-serif; font-weight: 700; font-size: 40px;
    letter-spacing: 2px; color: var(--ink);
  }
  .brand-mark { width: 40px; height: 40px; border-radius: 50%; background: var(--brand-blue); }
  .brand-tagline {
    margin: 4px 0 0 118px; font-family: Arimo, sans-serif; font-size: 8px;
    letter-spacing: 1px; color: #6b7080;
  }

  .web-banner {
    position: absolute; right: 0; top: 62px; width: 278px; height: 40px;
    background: var(--brand-blue);
    clip-path: polygon(0 0, 100% 0, 100% 100%, 11% 100%);
    display: flex; align-items: center; justify-content: flex-end; gap: 8px; padding-right: 24px;
    font-family: Arimo, sans-serif; font-weight: 700; font-size: 17px; color: var(--white);
  }

  .headline { position: absolute; left: 34px; top: 170px; }
  .headline .kicker { font-size: 17px; font-weight: 400; color: var(--ink); }
  .headline .year {
    font-size: 78px; font-weight: 700; color: var(--brand-blue); line-height: 0.95; margin-top: 6px;
    letter-spacing: -1px;
  }
  .headline .anniversary { font-size: 38px; font-weight: 700; color: var(--brand-blue); line-height: 1; }
  .headline .offer { font-size: 27px; font-weight: 400; color: var(--ink-soft); margin-top: 8px; }
  .headline .season {
    font-family: "League Spartan", sans-serif; font-weight: 700; font-size: 22px; color: var(--ink-soft);
    margin-top: 2px; letter-spacing: 0.3px;
  }
  .rule { position: absolute; left: 36px; top: 407px; width: 190px; height: 2px; background: var(--brand-blue-light); }

  .offer-block { position: absolute; left: 34px; top: 460px; }
  .offer-block .free {
    font-family: "League Spartan", sans-serif; font-weight: 800; font-size: 40px; line-height: 1;
    color: var(--brand-blue); letter-spacing: 0.5px;
  }
  .offer-block .terms { font-size: 24px; font-weight: 300; color: var(--ink-soft); margin-top: 2px; }

  .valid-box {
    position: absolute; left: 35px; top: 610px; width: 216px; height: 135px;
    border: 3px solid var(--brand-blue); text-align: center; color: var(--brand-blue);
  }
  .valid-box .label { font-size: 23px; font-weight: 400; margin-top: 8px; }
  .valid-box .dates {
    display: flex; align-items: center; justify-content: center; gap: 2px;
    font-family: "League Spartan", sans-serif; font-weight: 700; color: var(--ink);
    height: 66px;
  }
  .valid-box .day { font-size: 66px; line-height: 1; }
  .valid-box .dash { font-size: 56px; line-height: 1; margin: 0 4px; }
  .valid-box .month {
    writing-mode: vertical-rl; transform: rotate(180deg);
    font-family: "Josefin Sans", sans-serif; font-weight: 300; font-size: 24px; line-height: 1;
  }
  .valid-box .note {
    font-family: "League Spartan", sans-serif; font-weight: 700; font-size: 11px; color: var(--brand-blue);
    margin-top: 4px;
  }

  .benefits { position: absolute; left: 0; top: 0; width: 800px; height: 1200px; pointer-events: none; }
  .benefit { position: absolute; width: 130px; text-align: center; font-family: Arimo, sans-serif; font-size: 14px; line-height: 1.25; color: var(--ink); }
  .benefit .icon { width: 62px; height: 62px; border-radius: 50%; margin: 0 auto 12px; }

  .contact-bar {
    position: absolute; left: 27px; top: 1088px; width: 744px; height: 84px; background: var(--footer);
    display: flex; align-items: center; color: var(--white);
  }
  .contact-item { display: flex; align-items: center; gap: 10px; padding: 0 24px; }
  .contact-item + .contact-item { border-left: 2px solid var(--brand-blue-light); height: 46px; }
  .contact-phone { font-family: "Josefin Sans", sans-serif; font-weight: 600; font-size: 22px; width: 243px; }
  .contact-email { font-family: Arimo, sans-serif; font-size: 16px; width: 278px; justify-content: center; }
  .contact-address { font-family: Arimo, sans-serif; font-size: 10.5px; line-height: 1.35; }
  .contact-address .city { color: #8fb0ea; }
</style>
</head>
<body>
<main class="flyer">
  <div class="hero-backdrop"></div>
  <div class="hero-photo" role="img" aria-label="Photo of a hand holding a small white model house with a grey roof"></div>

  <svg class="swoosh" viewBox="0 0 800 180" preserveAspectRatio="none" aria-hidden="true">
    <path d="M0 60 Q400 250 800 0 L800 180 L0 180 Z" fill="var(--white)"/>
    <path d="M0 20 Q380 200 800 0 L800 12 Q420 260 0 48 Z" fill="var(--brand-blue)"/>
  </svg>

  <header class="brand">
    <div class="brand-name"><span class="brand-mark"></span>KVP LEASING</div>
    <div class="brand-tagline">KVP-LEASING.EXAMPLE &nbsp;|&nbsp; BY CORVANE</div>
  </header>

  <div class="web-banner">
    <svg width="17" height="17" viewBox="0 0 20 20" fill="none" stroke="#fff" stroke-width="1.5" aria-hidden="true">
      <circle cx="10" cy="10" r="8.5"/><ellipse cx="10" cy="10" rx="3.8" ry="8.5"/><path d="M1.5 10h17M3 5.5h14M3 14.5h14"/>
    </svg>
    kvp-leasing.example
  </div>

  <section class="headline">
    <p class="kicker">WE ARE CELEBRATING OUR</p>
    <h1 class="year">1-YEAR</h1>
    <p class="anniversary">ANNIVERSARY</p>
    <p class="offer">BY OFFERING A SPECIAL</p>
    <p class="season">PEAK-SEASON PROMOTION</p>
  </section>
  <div class="rule"></div>

  <section class="offer-block">
    <h2 class="free">FREE RENTALS<br>FOR 30 DAYS</h2>
    <p class="terms">WITH A MINIMUM 30-DAY RENTAL</p>
  </section>

  <section class="valid-box">
    <p class="label">VALID FROM</p>
    <div class="dates">
      <span class="day">1</span><span class="month">SEP</span>
      <span class="dash">–</span>
      <span class="day">31</span><span class="month">DEC</span>
    </div>
    <p class="note">AND WHILE SUPPLIES LAST</p>
  </section>

  <section class="benefits">
    <div class="benefit" style="left:15px; top:895px;"><div class="icon" role="img" aria-label="Icon of a rising bar chart" style="background:linear-gradient(135deg,#1f6f86,#f2b51c);"></div>Meet your<br>peak season<br>needs</div>
    <div class="benefit" style="left:137px; top:925px;"><div class="icon" role="img" aria-label="Icon of a magnifier over a chart" style="background:#e8566c;"></div>Be ready for<br>unforeseen surge<br>in demand</div>
    <div class="benefit" style="left:266px; top:945px;"><div class="icon" role="img" aria-label="Icon of a desk with a monitor" style="background:#f5c33b;"></div>Charters that<br>require off-the-<br>shelf equipment</div>
    <div class="benefit" style="left:402px; top:948px;"><div class="icon" role="img" aria-label="Icon of an hourglass" style="background:#2bb6d3;"></div>Bridge the<br>long-lead-time<br>gap of purchasing</div>
    <div class="benefit" style="left:538px; top:925px;"><div class="icon" role="img" aria-label="Icon of a piggy bank" style="background:#3d4453;"></div>Experience<br>budget flexibility</div>
    <div class="benefit" style="left:659px; top:893px;"><div class="icon" role="img" aria-label="Icon of balance scales" style="background:#3a3a5c;"></div>Re-balance<br>your ULD fleet</div>
  </section>

  <footer class="contact-bar">
    <div class="contact-item contact-phone">
      <svg width="20" height="20" viewBox="0 0 24 24" fill="none" stroke="#8fb0ea" stroke-width="2" aria-hidden="true">
        <path d="M5 3h4l2 5-2.5 1.5a11 11 0 0 0 6 6L16 13l5 2v4a2 2 0 0 1-2 2A17 17 0 0 1 3 5a2 2 0 0 1 2-2z"/>
      </svg>
      +1-555-284-3917
    </div>
    <div class="contact-item contact-email">
      <svg width="20" height="18" viewBox="0 0 24 20" fill="none" stroke="#8fb0ea" stroke-width="1.8" aria-hidden="true">
        <rect x="2" y="3" width="20" height="14" rx="1"/><path d="M2 4l10 7 10-7"/>
      </svg>
      rfq@kvp-leasing.example
    </div>
    <div class="contact-item contact-address">
      <svg width="16" height="20" viewBox="0 0 16 22" aria-hidden="true">
        <path d="M8 0a7 7 0 0 0-7 7c0 5 7 15 7 15s7-10 7-15a7 7 0 0 0-7-7z" fill="#6f97e0"/><circle cx="8" cy="7" r="2.6" fill="var(--footer)"/>
      </svg>
      <address style="font-style:normal; margin-left:8px;">
        <span class="city">Lakemont, CA (LKM)</span><br>88 Harbor Way<br>Lakemont, CA 90000
      </address>
    </div>
  </footer>
</main>
</body>
</html>
```